Tampa, Florida based Real Estate company Business Cards

Need ideas for real estate business cards
Updates

Need extra days to review

Industry/Entity Type

Real Estate

Contact Information for Business Card

Space for image, space for logo, contact information space

Font styles to use
Sans Serif

Colors

Designer to choose colors to be used in the design.

Requirements
Must have
• Options to have duplicate content on the back of card for a team of agents.

```html
<!DOCTYPE html>
<html lang="en">
<head>
<meta charset="utf-8">
<title>Harborline Homes – Business Cards</title>
<link rel="stylesheet" href="https://fonts.googleapis.com/css2?family=Roboto:wght@400;500;700&display=swap">
<style>
  :root {
    --navy: #1b1850;
    --accent-red: #e8384f;
    --silver: #c9c9cc;
    --paper: #ffffff;
    --backdrop: #e6e6e8;
    --ink-light: #ffffff;
  }
  * { margin: 0; padding: 0; box-sizing: border-box; }
  html, body {
    width: 1200px; height: 900px; overflow: hidden;
    background: var(--backdrop);
    font-family: "Roboto", Arial, sans-serif;
  }
  .sheet {
    width: 1200px; height: 900px;
    display: flex; flex-direction: column;
    align-items: center; justify-content: center; gap: 40px;
  }
  .card {
    position: relative;
    width: 700px; height: 400px;
    background: var(--paper);
    box-shadow: 0 10px 28px rgba(0,0,0,.18);
    overflow: hidden;
  }
  /* Front */
  .card--front { display: flex; align-items: center; justify-content: center; }
  .brand-name {
    font-weight: 700; color: var(--navy);
    font-size: 64px; letter-spacing: 2px;
    display: flex; align-items: center; gap: 20px;
  }
  .brand-name .brand-dot {
    width: 26px; height: 26px; border-radius: 50%; background: var(--navy);
  }
  /* Back */
  .card__shape { position: absolute; inset: 0; }
  .card__brand {
    position: absolute; left: 40px; top: 200px;
    width: 340px; text-align: center;
    transform: translate(0, -50%) rotate(-90deg);
    transform-origin: 110px 50%;
    font-weight: 700; color: var(--navy); font-size: 40px; letter-spacing: 1px;
  }
  .agent {
    position: absolute; left: 420px; top: 42px; right: 30px;
    color: var(--ink-light);
  }
  .agent__name { font-size: 30px; font-weight: 700; line-height: 1.1; }
  .agent__role { font-size: 24px; font-weight: 500; color: var(--accent-red); margin-top: 2px; }
  .contact { list-style: none; margin-top: 36px; }
  .contact__item {
    display: flex; align-items: center; gap: 12px;
    font-size: 14px; line-height: 1.2; margin-bottom: 16px;
  }
  .contact__icon {
    flex: 0 0 26px; width: 26px; height: 26px; border-radius: 50%;
    background: var(--ink-light);
    display: flex; align-items: center; justify-content: center;
  }
  .contact__icon svg { width: 15px; height: 15px; }
</style>
</head>
<body>
<main class="sheet">
  <section class="card card--front" aria-label="Card front">
    <div class="brand-name"><span class="brand-dot"></span>Harborline Homes</div>
  </section>

  <section class="card card--back" aria-label="Card back">
    <svg class="card__shape" viewBox="0 0 700 400" aria-hidden="true">
      <path d="M372 0 C360 140 370 280 430 400" fill="none" stroke="var(--silver)" stroke-width="10"/>
      <path d="M385 0 L700 0 L700 400 L448 400 C388 280 374 140 385 0 Z" fill="var(--navy)"/>
    </svg>
    <div class="card__brand">Harborline Homes</div>

    <div class="agent">
      <h1 class="agent__name">Tomasz Wielgosz</h1>
      <p class="agent__role">Agent</p>
      <ul class="contact">
        <li class="contact__item">
          <span class="contact__icon"><svg viewBox="0 0 24 24"><path d="M12 2a7 7 0 0 0-7 7c0 5 7 13 7 13s7-8 7-13a7 7 0 0 0-7-7zm0 9.5A2.5 2.5 0 1 1 12 6.5a2.5 2.5 0 0 1 0 5z" fill="var(--navy)"/></svg></span>
          <span>Rd.8 #2157, Near Palm Court<br>Sector 14B</span>
        </li>
        <li class="contact__item">
          <span class="contact__icon"><svg viewBox="0 0 24 24"><path d="M6.6 10.8a15 15 0 0 0 6.6 6.6l2.2-2.2a1 1 0 0 1 1-.25 11.4 11.4 0 0 0 3.6.57 1 1 0 0 1 1 1V20a1 1 0 0 1-1 1A17 17 0 0 1 3 4a1 1 0 0 1 1-1h3.5a1 1 0 0 1 1 1c0 1.25.2 2.45.57 3.6a1 1 0 0 1-.25 1z" fill="var(--navy)"/></svg></span>
          <span>555.014.2290</span>
        </li>
        <li class="contact__item">
          <span class="contact__icon"><svg viewBox="0 0 24 24"><rect x="3" y="5" width="18" height="14" rx="2" fill="none" stroke="var(--navy)" stroke-width="2"/><path d="M3.5 6l8.5 7 8.5-7" fill="none" stroke="var(--navy)" stroke-width="2"/></svg></span>
          <span>hello@harborlinehomes.com</span>
        </li>
        <li class="contact__item">
          <span class="contact__icon"><svg viewBox="0 0 24 24"><circle cx="12" cy="12" r="9" fill="none" stroke="var(--navy)" stroke-width="2"/><ellipse cx="12" cy="12" rx="4" ry="9" fill="none" stroke="var(--navy)" stroke-width="2"/><path d="M3 12h18" stroke="var(--navy)" stroke-width="2"/></svg></span>
          <span>www.harborlinehomes.com</span>
        </li>
      </ul>
    </div>
  </section>
</main>
</body>
</html>
```